We (R. T. Halvern & Associates, Inc.) are an executive Search firm based in Los Angeles that is exclusively focused in the Med Tech and Health Tech arenas.   I need a logo to communicate that we are a high end search firm, but also that we are focused in the medicine and science arenas called health tech and med tech.  Many of our clients have robotics and artificial intelligence type products, so it is very technology forward.  I tend to gravitate towards clean, sharp aesthetic as opposed to something that is really over the top.
Attached are files with my logo in two different layouts.  In addition to the letterhead and envelope, I also will need an electronic letterhead in Microsoft Word.  I tend to
I look forward to seeing the designs and just let me know if you have any questions.
Dale

```html
<!DOCTYPE html>
<html lang="en">
<head>
<meta charset="utf-8">
<title>R. T. Halvern &amp; Associates, Inc. — Stationery</title>
<link href="https://fonts.googleapis.com/css2?family=Montserrat:wght@400;600&display=swap" rel="stylesheet">
<style>
  :root {
    --backdrop: #d9d9d9;
    --paper: #ffffff;
    --flap-grey: #e6e7e9;
    --brand-blue: #52a3db;
    --ink: #111111;
    --text-grey: #555555;
    --shadow: rgba(0,0,0,0.35);
  }
  html, body {
    margin: 0;
    padding: 0;
    width: 1200px;
    height: 859px;
    overflow: hidden;
    background: var(--backdrop);
    font-family: 'Montserrat', Arial, sans-serif;
  }
  .board { position: relative; width: 1200px; height: 859px; }
  .sheet {
    position: absolute;
    background: var(--paper);
    box-shadow: 2px 3px 4px var(--shadow);
    overflow: hidden;
  }
  .letterhead { left: 61px; top: 49px; width: 583px; height: 754px; }

  .brand { position: absolute; display: flex; align-items: center; gap: 7px; }
  .brand-dot { width: 14px; height: 14px; border-radius: 50%; background: var(--brand-blue); flex: none; }
  .brand-name {
    font-weight: 600; color: var(--ink); line-height: 1.05; letter-spacing: 0.02em;
  }
  .brand-name .line2 { display: block; font-size: 0.45em; letter-spacing: 0.25em; margin-top: 2px; }

  .letterhead .brand { left: 40px; top: 120px; }
  .letterhead .brand-name { font-size: 17px; }

  .contact {
    position: absolute; right: 40px; top: 40px;
    text-align: right; font-size: 9.5px; color: var(--text-grey); line-height: 11.6px;
  }
  .contact p { margin: 0; }
  .contact .address { margin-bottom: 5px; }
  .contact .row { display: flex; justify-content: flex-end; align-items: center; gap: 4px; }
  .contact svg { width: 7px; height: 7px; fill: var(--brand-blue); }
  .accent-bar {
    position: absolute; right: 0; top: 43px; width: 7px; height: 70px; background: var(--brand-blue);
  }

  .swoosh { position: absolute; left: 0; bottom: 0; width: 100%; }
  .letterhead .swoosh { height: 89px; }
  .swoosh .blue { fill: var(--brand-blue); }
  .swoosh .black { fill: var(--ink); }

  .envelope-back-grey { left: 688px; top: 50px; width: 450px; height: 279px; }
  .envelope-back-grey .flap {
    position: absolute; left: 0; top: 0; width: 100%; height: 67px;
  }
  .envelope-back-white { left: 687px; top: 353px; width: 452px; height: 212px; }
  .envelope-back-white .flap {
    position: absolute; left: 0; top: 0; width: 100%; height: 68px;
  }
  .flap-brand { left: 50%; transform: translateX(-50%); }
  .envelope-back-grey .flap-brand { top: 22px; }
  .envelope-back-white .flap-brand { top: 23px; }
  .flap-brand .brand-name { font-size: 12px; }
  .flap-brand .brand-dot { width: 10px; height: 10px; }

  .envelope-front { left: 687px; top: 587px; width: 452px; height: 214px; }
  .envelope-front .brand { left: 23px; top: 24px; }
  .envelope-front .brand-name { font-size: 12px; }
  .envelope-front .brand-dot { width: 10px; height: 10px; }
  .return-address {
    position: absolute; left: 23px; top: 61px; margin: 0;
    font-size: 7px; line-height: 9px; color: var(--text-grey);
  }
  .envelope-front .swoosh { height: 76px; }
</style>
</head>
<body>
<main class="board">

  <section class="sheet letterhead" aria-label="Letterhead">
    <div class="brand">
      <span class="brand-dot"></span>
      <span class="brand-name">R. T. HALVERN<span class="line2">&amp; ASSOCIATES INC.</span></span>
    </div>

    <div class="contact">
      <p class="address">1180 Larchmont Avenue<br>Fairview, WI 53190</p>
      <p class="row">+49(4)421-70 31825
        <svg viewBox="0 0 10 10"><path d="M2 0.5 L3.8 2.5 L2.8 3.6 Q4 6 6.4 7.2 L7.5 6.2 L9.5 8 L8.3 9.5 Q1 8.5 0.5 1.7Z"/></svg></p>
      <p class="row">+49(0)162-5538104
        <svg viewBox="0 0 10 10"><rect x="2.5" y="0.5" width="5" height="2.5"/><rect x="0.5" y="3.5" width="9" height="4" rx="1"/><rect x="2.5" y="7" width="5" height="2.5"/></svg></p>
      <p class="row">contact@halvernassoc.com
        <svg viewBox="0 0 10 10"><path d="M0.5 2 H9.5 V8.5 H0.5 Z M1.5 3 V7.5 H8.5 V3 L5 5.6 Z" fill-rule="evenodd"/></svg></p>
      <p class="row">www.halvernassoc.com
        <svg viewBox="0 0 10 10"><circle cx="5" cy="5" r="4.5"/></svg></p>
    </div>
    <div class="accent-bar"></div>

    <svg class="swoosh" viewBox="0 0 972 148" preserveAspectRatio="none" aria-hidden="true">
      <path class="black" d="M0 67 Q450 142 820 88 Q450 126 0 86 Z"/>
      <path class="blue" d="M100 78 Q600 112 972 0 L972 38 Q600 128 100 78 Z"/>
      <path class="blue" d="M0 95 Q486 175 972 45 L972 148 L0 148 Z"/>
    </svg>
  </section>

  <section class="sheet envelope-back-grey" aria-label="Envelope back, grey flap">
    <svg class="flap" viewBox="0 0 450 67" preserveAspectRatio="none" aria-hidden="true">
      <path d="M0 67 L17 5 Q19 0 25 0 L425 0 Q431 0 433 5 L450 67 Z" fill="var(--flap-grey)"/>
    </svg>
    <div class="brand flap-brand">
      <span class="brand-dot"></span>
      <span class="brand-name">R. T. HALVERN<span class="line2">&amp; ASSOCIATES INC.</span></span>
    </div>
  </section>

  <section class="sheet envelope-back-white" aria-label="Envelope back, white flap">
    <svg class="flap" viewBox="0 0 452 68" preserveAspectRatio="none" aria-hidden="true">
      <path d="M0 0 L17 60 Q20 67 27 67 L425 67 Q432 67 435 60 L452 0" fill="none" stroke="#c8c8c8" stroke-width="1.2"/>
    </svg>
    <div class="brand flap-brand">
      <span class="brand-dot"></span>
      <span class="brand-name">R. T. HALVERN<span class="line2">&amp; ASSOCIATES INC.</span></span>
    </div>
  </section>

  <section class="sheet envelope-front" aria-label="Envelope front">
    <div class="brand">
      <span class="brand-dot"></span>
      <span class="brand-name">R. T. HALVERN<span class="line2">&amp; ASSOCIATES INC.</span></span>
    </div>
    <p class="return-address">1180 Larchmont Avenue<br>Fairview, WI 53190</p>
    <svg class="swoosh" viewBox="0 0 972 148" preserveAspectRatio="none" aria-hidden="true">
      <path class="black" d="M0 67 Q450 142 820 88 Q450 126 0 86 Z"/>
      <path class="blue" d="M100 78 Q600 112 972 0 L972 38 Q600 128 100 78 Z"/>
      <path class="blue" d="M0 95 Q486 175 972 45 L972 148 L0 148 Z"/>
    </svg>
  </section>

</main>
</body>
</html>
```